New Business Card for Innovative Tool Company

We need a new design of business card for our florida based tool manufacturing company. I will attach 2 files that we use for our logo, use whichever you feel works best for the card. Main colours are as per logo, and we can use different shades of black/white/grey for the background.

Contact Information for Business Card

Name/Jobtitle/cell
Brackwell Tools
Suite 214c
3190 Harlowmere Pkw
Marlow Bay, FL30417
USA
name@brackwellco.example
www.brackwellco.example

Font styles to use
Sans Serif

Colors

Designer to choose colors to be used in the design.

Requirements
Must have
• Icons for Chatterly, Quiplet, Snapvista, Findora & Viewtube

```html
<!DOCTYPE html>
<html lang="en">
<head>
<meta charset="utf-8">
<title>Brackwell Tools — Business Card</title>
<link href="https://fonts.googleapis.com/css2?family=Arimo:wght@400;700&display=swap" rel="stylesheet">
<style>
  :root {
    --backdrop: #d6d6d6;
    --card-dark: #54575a;
    --card-light: #75787b;
    --ink: #ffffff;
    --ink-soft: rgba(255,255,255,0.85);
    --ghost: rgba(255,255,255,0.12);
  }
  * { box-sizing: border-box; margin: 0; padding: 0; }
  html, body {
    width: 1200px; height: 960px; overflow: hidden;
    background: var(--backdrop);
    font-family: "Arimo", Arial, sans-serif;
    color: var(--ink);
  }
  .card-set { position: relative; width: 1200px; height: 960px; }
  .card {
    position: absolute; top: 364px;
    width: 430px; height: 240px;
    background:
      radial-gradient(ellipse 65% 50% at 50% 12%, var(--card-light), transparent 75%),
      linear-gradient(160deg, var(--card-dark) 0%, #606366 45%, var(--card-dark) 100%);
  }

  /* Front */
  .card--front { left: 110px; }
  .brand-mark {
    position: absolute; left: 177px; top: 50px;
    width: 78px; height: 78px; border-radius: 50%;
    border: 1.5px solid var(--ink-soft);
  }
  .brand-name {
    position: absolute; left: 0; right: 0; top: 136px; text-align: center;
    font-weight: 700; font-size: 34px; letter-spacing: 3px; line-height: 1;
  }
  .brand-sub {
    position: absolute; left: 0; right: 0; top: 174px; text-align: center;
    font-weight: 700; font-size: 14px; letter-spacing: 16px; padding-left: 16px; line-height: 1;
  }

  /* Back */
  .card--back { left: 638px; height: 246px; }
  .identity__ghost {
    position: absolute; left: 54px; top: 80px;
    width: 72px; height: 72px; border-radius: 50%;
    border: 3px solid var(--ghost);
  }
  .identity__name {
    position: absolute; left: 14px; width: 180px; top: 100px; text-align: center;
    font-size: 18px; letter-spacing: 0.3px; line-height: 1;
  }
  .identity__title {
    position: absolute; left: 14px; width: 180px; top: 123px; text-align: center;
    font-size: 8.5px; letter-spacing: 0.3px; line-height: 1;
  }
  .divider {
    position: absolute; left: 192px; top: 54px;
    width: 2px; height: 130px; background: var(--ink);
  }
  .contact-item {
    position: absolute; left: 228px;
    display: flex; align-items: flex-start; gap: 10px;
    font-size: 7px; line-height: 1.2;
  }
  .contact-item svg { width: 14px; height: 14px; flex: none; margin-top: -3px; }
  .contact-item--phone { top: 68px; }
  .contact-item--mail { top: 92px; }
  .contact-item--web { top: 117px; }
  .contact-item--address { top: 142px; }
  .social-row {
    position: absolute; left: 92px; width: 200px; top: 205px;
    display: flex; justify-content: center; gap: 7px;
    font-size: 7.5px; font-weight: 700; line-height: 1;
  }
</style>
</head>
<body>
<main class="card-set">
  <section class="card card--front" aria-label="Card front">
    <div class="brand-mark"></div>
    <div class="brand-name">BRACKWELL</div>
    <div class="brand-sub">TOOLS</div>
  </section>

  <section class="card card--back" aria-label="Card back">
    <div class="identity__ghost"></div>
    <div class="identity__name">ALAN REEVE</div>
    <div class="identity__title">FOUNDER &amp; CEO</div>
    <div class="divider"></div>

    <div class="contact-item contact-item--phone">
      <svg viewBox="0 0 16 16" fill="#fff"><path d="M3 1.5l3 .5 1 3.2-1.7 1.4a9 9 0 0 0 4.1 4.1L10.8 9l3.2 1 .5 3-1.8 1.7C7.5 14.5 1.5 8.5 1.3 3.3z"/></svg>
      <span>+004127650914</span>
    </div>
    <div class="contact-item contact-item--mail">
      <svg viewBox="0 0 16 16" fill="none" stroke="#fff" stroke-width="1.1"><rect x="1.5" y="3.5" width="13" height="9"/><path d="M1.5 3.5 8 9l6.5-5.5"/></svg>
      <span>alan.reeve@brackwellco.example</span>
    </div>
    <div class="contact-item contact-item--web">
      <svg viewBox="0 0 16 16" fill="none" stroke="#fff" stroke-width="1.1"><circle cx="8" cy="8" r="6.5"/><ellipse cx="8" cy="8" rx="3" ry="6.5"/><path d="M1.5 8h13M2.5 5h11M2.5 11h11"/></svg>
      <span>www.brackwellco.example</span>
    </div>
    <div class="contact-item contact-item--address">
      <svg viewBox="0 0 16 16" fill="#fff"><path d="M8 1a5 5 0 0 0-5 5c0 4 5 9.5 5 9.5S13 10 13 6a5 5 0 0 0-5-5zm0 7a2 2 0 1 1 0-4 2 2 0 0 1 0 4z"/></svg>
      <span>Brackwell Tools<br>Suite 214c<br>3190 Harlowmere Pkw<br>Marlow Bay, FL30417<br>USA</span>
    </div>

    <div class="social-row">
      <span>Chatterly</span><span>Quiplet</span><span>Snapvista</span><span>Findora</span><span>Viewtube</span>
    </div>
  </section>
</main>
</body>
</html>
```